Lose Up To 1 LB Of Fat Per Day

We need a double sided street sign for our weight loss clinic. We need the doctors picture to the right side of the sign and we need a challenge “Lose Up To 1 Pound Of Fat Per Day” included in the signage.
Our color scheme for the clinic are black, white, teal and silver.
The phone number should be at the bottom of the sign
555-206–3948

Target Market(s)

Weight Loss

Font styles to use
Sans Serif

```html
<!DOCTYPE html>
<html lang="en">
<head>
<meta charset="utf-8">
<title>Lose Up To 1 Pound Of Fat Per Day – Street Sign</title>
<link href="https://fonts.googleapis.com/css2?family=Barlow+Condensed:ital,wght@1,700;1,800&family=Roboto:wght@400;700&display=swap" rel="stylesheet">
<style>
  :root {
    --page: #ffffff;
    --pink-top: #dc7ec0;
    --violet-mid: #a05fd6;
    --indigo-deep: #4a1cc6;
    --white: #ffffff;
    --fat-pink: #e07aa8;
    --fat-panel: #fbeef7;
    --suit-dark: #1d1e26;
  }
  * { margin: 0; padding: 0; box-sizing: border-box; }
  html, body {
    width: 1200px; height: 826px; overflow: hidden;
    background: var(--page);
  }
  .sign {
    position: absolute; left: 80px; top: 124px;
    width: 1040px; height: 579px; overflow: hidden;
    background: linear-gradient(165deg, var(--pink-top) 0%, var(--violet-mid) 45%, var(--indigo-deep) 100%);
  }
  .sign-backdrop, .doctor-photo { position: absolute; left: 0; top: 0; }
  .headline {
    position: absolute; inset: 0;
    font-family: "Barlow Condensed", sans-serif;
    font-style: italic; color: var(--white);
    text-transform: uppercase; line-height: 1;
  }
  .headline-lead {
    position: absolute; left: 172px; top: 24px;
    font-size: 80px; font-weight: 700; white-space: nowrap; letter-spacing: 6px;
  }
  .headline-main {
    position: absolute; left: 36px; top: 86px;
    font-size: 190px; font-weight: 800; white-space: nowrap; letter-spacing: -1px;
    transform: scaleX(0.86); transform-origin: left top;
  }
  .headline-tail {
    position: absolute; left: 61px; top: 259px; height: 120px;
    display: flex; align-items: center; white-space: nowrap;
  }
  .fat-tag {
    height: 120px; width: 195px;
    background: var(--fat-panel);
    clip-path: polygon(0 0, 100% 0, 88% 100%, 0 100%);
    color: var(--fat-pink);
    font-size: 147px; font-weight: 800;
    display: flex; align-items: center; padding-left: 12px;
  }
  .per-day {
    font-size: 147px; font-weight: 800; margin-left: -6px;
  }
  .phone {
    position: absolute; left: 31px; top: 490px;
    display: flex; align-items: center; gap: 14px;
    font-family: "Roboto", sans-serif; font-weight: 700;
    font-size: 63px; line-height: 1; color: var(--white); letter-spacing: -2px;
  }
  .phone-icon { width: 56px; height: 58px; }
  .doctor-name {
    position: absolute; right: 24px; top: 526px;
    font-family: "Roboto", sans-serif; font-weight: 400;
    font-size: 27px; line-height: 1; color: var(--white); white-space: nowrap;
  }
</style>
</head>
<body>
  <div class="sign">
    <svg class="sign-backdrop" width="1040" height="579" viewBox="0 0 1040 579" aria-hidden="true">
      <path d="M695 0 L975 0 C975 200 930 330 850 420 L700 470 Z" fill="#7a2bb0" fill-opacity="0.45"/>
      <path d="M975 0 L1040 0 L1040 579 L850 579 L850 420 C930 330 975 200 975 0 Z" fill="#ffffff" fill-opacity="0.12"/>
      <ellipse cx="290" cy="110" rx="425" ry="363" fill="#ffffff" fill-opacity="0.1"/>
      <ellipse cx="290" cy="100" rx="405" ry="351" fill="none" stroke="#ffffff" stroke-opacity="0.3" stroke-width="3"/>
    </svg>

    <svg class="doctor-photo" width="1040" height="579" viewBox="0 0 1040 579" role="img" aria-label="Portrait photo of the clinic's doctor in a dark suit, white shirt and purple tie">
      <defs>
        <linearGradient id="photoTone" x1="0" y1="0" x2="0" y2="1">
          <stop offset="0" stop-color="#b98a7a"/>
          <stop offset="0.42" stop-color="#a6786e"/>
          <stop offset="0.55" stop-color="#2a2a36"/>
          <stop offset="1" stop-color="#1d1e26"/>
        </linearGradient>
      </defs>
      <path d="M770 14 C830 14 860 60 860 130 C860 190 850 240 850 270 L1040 330 L1040 579 L514 579 C530 480 545 400 562 360 C600 300 660 280 700 270 C695 240 680 190 680 130 C680 60 710 14 770 14 Z" fill="url(#photoTone)"/>
    </svg>

    <div class="headline">
      <div class="headline-lead">Lose up to</div>
      <div class="headline-main">1 Pound of</div>
      <div class="headline-tail">
        <span class="fat-tag">Fat</span>
        <span class="per-day">Per Day</span>
      </div>
    </div>

    <div class="phone">
      <svg class="phone-icon" viewBox="0 0 64 64" aria-hidden="true">
        <path d="M14 6 C10 8 6 12 6 18 C8 34 26 54 44 58 C50 58 54 54 56 50 L46 40 C43 42 40 44 38 44 C30 40 24 32 20 26 C20 24 22 21 24 18 Z" fill="none" stroke="#ffffff" stroke-width="4" stroke-linejoin="round"/>
        <path d="M36 22 a8 8 0 0 1 6 6" fill="none" stroke="#ffffff" stroke-width="3.5" stroke-linecap="round"/>
        <path d="M38 12 a18 18 0 0 1 14 14" fill="none" stroke="#ffffff" stroke-width="3.5" stroke-linecap="round"/>
        <path d="M40 2 a28 28 0 0 1 22 22" fill="none" stroke="#ffffff" stroke-width="3.5" stroke-linecap="round"/>
      </svg>
      <span class="phone-number">555-206–3948</span>
    </div>

    <div class="doctor-name">DR.DANIEL MARSH</div>
  </div>
</body>
</html>
```